“We’re Hiring” Canva Template for LinkedIn Posts

We’re looking for a modern, eye-catching LinkedIn post template that we can easily reuse whenever we announce new job openings.
The final design must be editable in Canva so that our marketing team can update the position title, location, and hiring manager information for future hires.

Key Requirements:
Format: Canva Template (editable)
Primary Logo: ORLA Graft KT
Secondary Logo: Tarrow Biologics (can appear smaller, e.g., bottom corner)
Headline Options: “We’re Hiring” or “Join Our Team”

Editable Text Fields:
Job Title
Location (City / State)
Hiring Manager’s Name
Hiring Manager’s Email (with clear direction such as “Email [Name] at [Email] to apply”)

Design Style:
Tone: Professional, clean, and modern
Color Palette: Use ORLA Graft KT brand colors prominently (Tarrow secondary accent is fine)
Layout: Easy to read at a glance when scrolling LinkedIn
Aesthetic Keywords: Polished, credible, corporate, but visually appealing
Font Style: Clean sans-serif fonts preferred (modern and readable)

Design Inspiration:
We’d like something that feels in line with modern biotech/medical device marketing—professional but visually sharp. Examples include layouts with:
A hero headline at the top (“We’re Hiring” / “Join Our Team”)
Company logo lockup with hierarchy (ORLA Graft KT primary, Tarrow secondary)
A clear call-to-action section for the hiring manager’s contact
Optional background texture or subtle gradient using brand colors

Usage:
This template will be used primarily for LinkedIn and other professional social media posts, so designs should be optimized for 1920 x 1080 pixels (portrait) or 1080 x 1080 pixels (square).

```html
<!DOCTYPE html>
<html lang="en">
<head>
<meta charset="utf-8">
<title>We Are Hiring – ORLA Graft KT</title>
<link href="https://fonts.googleapis.com/css2?family=League+Spartan:wght@500;600;700;800&display=swap" rel="stylesheet">
<style>
  :root {
    --magenta: #a8208f;
    --navy: #0e1a45;
    --white: #ffffff;
    --green-light: #9dcd5e;
    --green-mid: #8fc35a;
    --green-dark: #6d9a50;
    --earth: #a88a78;
  }
  * { margin: 0; padding: 0; box-sizing: border-box; }
  html, body { width: 1200px; height: 1200px; overflow: hidden; }
  body { font-family: "League Spartan", Arial, sans-serif; }

  .post {
    position: relative;
    width: 1200px;
    height: 1200px;
    overflow: hidden;
    background:
      radial-gradient(ellipse 620px 560px at 1150px 40px, var(--green-dark) 0%, rgba(109,154,80,0) 100%),
      radial-gradient(ellipse 620px 700px at -40px 1100px, var(--earth) 0%, rgba(168,138,120,0) 100%),
      linear-gradient(135deg, var(--green-light) 0%, var(--green-mid) 60%, var(--green-light) 100%);
  }

  .brand-primary, .brand-secondary {
    position: absolute;
    top: 70px;
    color: var(--white);
    font-weight: 600;
    letter-spacing: 0.5px;
  }
  .brand-primary { left: 84px; font-size: 40px; line-height: 1; }
  .brand-secondary { right: 92px; font-size: 40px; line-height: 1; }

  .headline { position: absolute; left: 128px; color: var(--magenta); font-weight: 700; line-height: 1; }
  .headline-top { top: 222px; font-size: 108px; letter-spacing: -1px; }
  .headline-main { top: 330px; font-size: 232px; letter-spacing: -4px; }

  .info-card {
    position: absolute;
    left: 78px; top: 550px;
    width: 1058px; height: 481px;
    background: var(--white);
    border-radius: 44px;
  }

  .position-tag {
    position: absolute;
    left: 158px; top: 600px;
    width: 359px; height: 86px;
    border-radius: 43px;
    background: var(--magenta);
    color: var(--navy);
    font-size: 33px; font-weight: 700;
    display: flex; align-items: center; justify-content: center;
    padding-top: 4px;
  }
  .job-title {
    position: absolute;
    left: 100px; top: 722px; width: 480px;
    text-align: center;
    color: var(--navy);
    font-size: 40px; font-weight: 700;
  }
  .location-label {
    position: absolute; left: 144px; top: 846px;
    color: var(--magenta); font-size: 33px; font-weight: 700;
  }
  .location-address {
    position: absolute; left: 144px; top: 890px;
    color: var(--navy); font-size: 33px; font-weight: 700; line-height: 44px;
  }

  .divider { position: absolute; left: 586px; top: 604px; }

  .contact-lead {
    position: absolute; left: 637px; top: 600px;
    color: var(--navy); font-size: 71px; font-weight: 700; line-height: 72px;
  }
  .contact-name {
    position: absolute; left: 634px; top: 766px;
    color: var(--magenta); font-size: 46px; font-weight: 700;
  }
  .contact-email {
    position: absolute; left: 645px; top: 832px;
    color: var(--navy); font-size: 30px; font-weight: 500;
    text-decoration: underline; text-underline-offset: 4px;
  }

  .apply-button {
    position: absolute;
    left: 637px; top: 958px;
    width: 474px; height: 123px;
    border-radius: 62px;
    background: var(--magenta);
    color: var(--navy);
    font-size: 54px; font-weight: 700;
    display: flex; align-items: center; justify-content: center;
    padding-top: 6px;
    box-shadow: 0 8px 26px rgba(0,0,0,0.28);
  }
</style>
</head>
<body>
  <main class="post">
    <div class="brand-primary">ORLA Graft KT</div>
    <div class="brand-secondary">TARROW</div>

    <h1>
      <span class="headline headline-top">We Are</span>
      <span class="headline headline-main">Hiring!</span>
    </h1>

    <section class="info-card" aria-hidden="true"></section>

    <div class="position-tag">OPEN POSITION</div>
    <div class="job-title">BioMedical Engineer</div>
    <div class="location-label">LOCATION:</div>
    <div class="location-address">TechPark 4, Alder St.<br>Colorado, USA</div>

    <svg class="divider" width="24" height="380" viewBox="0 0 24 380" aria-hidden="true">
      <line x1="12" y1="12" x2="12" y2="368" stroke="#0e1a45" stroke-width="3"/>
      <circle cx="12" cy="10" r="7" fill="#ffffff" stroke="#0e1a45" stroke-width="3"/>
      <circle cx="12" cy="370" r="7" fill="#ffffff" stroke="#0e1a45" stroke-width="3"/>
    </svg>

    <div class="contact-lead">Send your<br>Resume to</div>
    <div class="contact-name">Dana R. Hale</div>
    <div class="contact-email">danarhale@orlagraft.com</div>

    <div class="apply-button">APPLY NOW!</div>
  </main>
</body>
</html>
```